Breakfast Briefings / Lunch & Learn

I would like to have a double sided flyer size 8x10 to display the breakfast briefing on one side and Lunch & Learn on the other side.

Header on each side to say
2018 Calendar Breakfast Briefing (on the breakfast side)
2018 Calendar Lunch & Learn (on the lunch side)

I have attached a copy of the files we would like to use.

Learn

```html
<!DOCTYPE html>
<html lang="en">
<head>
<meta charset="utf-8">
<title>2018 Calendar – Breakfast Briefing / Lunch &amp; Learn</title>
<link rel="stylesheet" href="https://fonts.googleapis.com/css2?family=Montserrat:wght@400;500;600;700;800&family=Exo+2:wght@400;500;600;700&display=swap">
<style>
  :root {
    --stage: #cdcdcd;
    --paper: #ffffff;
    --ink: #111111;
    --brand-blue: #1a7bbf;
    --logo-grey: #555b60;
    --sky: #2aa9e0;
    --board-dark: #2e2f36;
    --board-mid: #4a4b55;
    --band-teal: #1d8f82;
    --white: #ffffff;
    --c-medical: #2f9fae;
    --c-sales: #53b6b4;
    --c-finance: #e4b445;
    --c-rnd: #e6c27c;
    --c-ops: #e98a26;
    --c-clinical: #c98a3e;
    --c-quality: #d6435a;
    --c-people: #c0384f;
    --c-marketing: #1d4f7a;
    --c-legal: #1f6ea5;
    --c-access: #2b85b8;
    --c-tos: #4fb1e0;
  }
  * { box-sizing: border-box; margin: 0; padding: 0; }
  html, body { width: 1014px; height: 1200px; overflow: hidden; }
  body { background: var(--stage); position: relative; font-family: "Montserrat", sans-serif; }

  .flyer {
    position: absolute; top: 306px; width: 470px; height: 588px; overflow: hidden;
    box-shadow: 0 4px 14px rgba(0,0,0,.25);
  }
  .flyer--breakfast { left: 24px; background: var(--paper); }
  .flyer--lunch { left: 520px; background: var(--band-teal); font-family: "Exo 2", sans-serif; }

  .brand { position: absolute; display: flex; align-items: center; gap: 8px; }
  .brand__mark { width: 14px; height: 14px; }
  .brand__name { font-family: "Montserrat", sans-serif; font-weight: 500; font-size: 22px; letter-spacing: 4px; }
  .flyer--breakfast .brand { top: 32px; left: 0; right: 0; justify-content: center; }
  .flyer--breakfast .brand__mark { background: var(--brand-blue); }
  .flyer--breakfast .brand__name { color: var(--logo-grey); }
  .flyer--lunch .brand { top: 40px; left: 29px; }
  .flyer--lunch .brand__mark { background: var(--white); }
  .flyer--lunch .brand__name { color: var(--white); }

  .breakfast-title { position: absolute; top: 92px; left: 0; right: 0; text-align: center; line-height: 1.05; }
  .breakfast-title__year { display: block; font-size: 28px; font-weight: 700; color: var(--ink); }
  .breakfast-title__event { display: block; font-size: 29px; font-weight: 800; color: var(--brand-blue); letter-spacing: .5px; }

  .wheel { position: absolute; top: 170px; left: 0; }
  .seg-dept, .seg-name { font-family: "Montserrat", sans-serif; font-size: 6.5px; fill: var(--white); text-anchor: middle; }
  .seg-name { font-weight: 600; }
  .seg-month { font-family: "Montserrat", sans-serif; font-size: 8.5px; font-weight: 700; fill: var(--white); text-anchor: middle; }
  .device-year { font-family: "Montserrat", sans-serif; font-size: 7.5px; fill: var(--brand-blue); text-anchor: middle; font-weight: 500; }
  .device-event { font-family: "Montserrat", sans-serif; font-size: 7px; font-weight: 800; fill: var(--ink); text-anchor: middle; }

  .lunch-photo {
    position: absolute; top: 0; left: 0; width: 470px; height: 384px;
    background: linear-gradient(90deg, var(--board-dark) 0%, var(--board-mid) 55%, #6b5a48 78%, #8a6d4d 100%);
  }
  .lunch-title { position: absolute; top: 106px; left: 29px; color: var(--white); }
  .lunch-title__year { display: block; font-size: 35px; font-weight: 600; color: var(--sky); line-height: 1.2; }
  .lunch-title__event { display: block; font-size: 35px; font-weight: 700; line-height: 1.25; }
  .lunch-title__tag { display: block; font-size: 13px; margin-top: 6px; }

  .schedule { position: absolute; top: 384px; left: 0; width: 470px; height: 204px; }
  .session { position: absolute; color: var(--white); width: 140px; }
  .session__month { display: block; font-size: 14px; font-weight: 600; letter-spacing: .5px; line-height: 1.1; }
  .session__topic { display: block; font-family: "Montserrat", sans-serif; font-size: 7.5px; line-height: 1.35; }
  .col-1 { left: 29px; } .col-2 { left: 180px; } .col-3 { left: 332px; }
  .row-1 { top: 23px; } .row-2 { top: 84px; } .row-3 { top: 152px; }
  .col-3.row-1 { top: 23px; } .col-3.row-2 { top: 70px; } .col-3.row-3 { top: 117px; }
  .col-3.row-4 { top: 163px; }
</style>
</head>
<body>

<section class="flyer flyer--breakfast">
  <div class="brand"><span class="brand__mark"></span><span class="brand__name">VELTRA</span></div>
  <h1 class="breakfast-title">
    <span class="breakfast-title__year">2018 Calendar</span>
    <span class="breakfast-title__event">BREAKFAST BRIEFING</span>
  </h1>

  <svg class="wheel" width="470" height="400" viewBox="0 0 470 400">
    <defs>
      <path id="sector" d="M -42.34 -169.8 A 175 175 0 0 1 42.34 -169.8 L 21.29 -85.39 A 88 88 0 0 0 -21.29 -85.39 Z"/>
      <radialGradient id="wood" cx="50%" cy="45%" r="60%">
        <stop offset="0" stop-color="#b98a5c"/>
        <stop offset="1" stop-color="#8a5f3a"/>
      </radialGradient>
      <radialGradient id="floor-shadow" cx="50%" cy="50%" r="50%">
        <stop offset="0" stop-color="#000" stop-opacity=".22"/>
        <stop offset="1" stop-color="#000" stop-opacity="0"/>
      </radialGradient>
    </defs>
    <ellipse cx="235" cy="385" rx="170" ry="4" fill="url(#floor-shadow)"/>
    <g transform="translate(235 187)">
      <use href="#sector" fill="var(--c-medical)"/>
      <use href="#sector" fill="var(--c-sales)" transform="rotate(30)"/>
      <use href="#sector" fill="var(--c-finance)" transform="rotate(60)"/>
      <use href="#sector" fill="var(--c-rnd)" transform="rotate(90)"/>
      <use href="#sector" fill="var(--c-ops)" transform="rotate(120)"/>
      <use href="#sector" fill="var(--c-clinical)" transform="rotate(150)"/>
      <use href="#sector" fill="var(--c-quality)" transform="rotate(180)"/>
      <use href="#sector" fill="var(--c-people)" transform="rotate(210)"/>
      <use href="#sector" fill="var(--c-marketing)" transform="rotate(240)"/>
      <use href="#sector" fill="var(--c-legal)" transform="rotate(270)"/>
      <use href="#sector" fill="var(--c-access)" transform="rotate(300)"/>
      <use href="#sector" fill="var(--c-tos)" transform="rotate(330)"/>

      <g transform="translate(0 -132)"><text class="seg-dept" y="-9">Medical</text><text class="seg-name" y="-1">Mark Ellison</text><text class="seg-month" y="10">2019 TBD</text></g>
      <g transform="translate(66 -114.3)"><text class="seg-dept" y="-9">Sales</text><text class="seg-name" y="-1">Tom Redford</text><text class="seg-month" y="10">2019 TBD</text></g>
      <g transform="translate(114.3 -66)"><text class="seg-dept" y="-9">Finance</text><text class="seg-name" y="-1">Paul Hendry</text><text class="seg-month" y="10">MARCH</text></g>
      <g transform="translate(132 0)"><text class="seg-dept" y="-9">R&amp;D</text><text class="seg-name" y="-1">Nina Halvorsen</text><text class="seg-month" y="10">APRIL</text></g>
      <g transform="translate(114.3 66)"><text class="seg-dept" y="-9">Operations</text><text class="seg-name" y="-1">Owen Callister</text><text class="seg-month" y="10">MAY</text></g>
      <g transform="translate(66 114.3)"><text class="seg-dept" y="-9">Clinical/ Reg</text><text class="seg-name" y="-1">Sean Maddox</text><text class="seg-month" y="10">JUNE</text></g>
      <g transform="translate(0 132)"><text class="seg-dept" y="-9">Quality</text><text class="seg-name" y="-1">Grant Whitlow</text><text class="seg-month" y="10">JULY</text></g>
      <g transform="translate(-66 114.3)"><text class="seg-dept" y="-9">People</text><text class="seg-name" y="-1">Priya Nandan</text><text class="seg-month" y="10">AUGUST</text></g>
      <g transform="translate(-114.3 66)"><text class="seg-dept" y="-9">Marketing</text><text class="seg-name" y="-1">Arjun Mehra</text><text class="seg-month" y="10">SEPTEMBER</text></g>
      <g transform="translate(-132 0)"><text class="seg-dept" y="-9">Legal</text><text class="seg-name" y="-1">Omar Haddad</text><text class="seg-month" y="10">OCTOBER</text></g>
      <g transform="translate(-114.3 -66)"><text class="seg-dept" y="-9">Market Access</text><text class="seg-name" y="-1">Helen Vasquez</text><text class="seg-month" y="10">NOVEMBER</text></g>
      <g transform="translate(-66 -114.3)"><text class="seg-dept" y="-9">TOS</text><text class="seg-name" y="-1">Laura Bennet</text><text class="seg-month" y="10">DECEMBER</text></g>

      <circle r="84" fill="url(#wood)" role="img" aria-label="Photo of a wooden table set with a fork and knife"/>
      <rect x="-37" y="-22" width="74" height="44" rx="5" fill="#111"/>
      <rect x="-32" y="-17" width="64" height="34" rx="1.5" fill="var(--paper)"/>
      <text class="device-year" y="-6">2018 Calendar</text>
      <text class="device-event" y="3">BREAKFAST</text>
      <text class="device-event" y="11">BRIEFING</text>
    </g>
  </svg>
</section>

<section class="flyer flyer--lunch">
  <div class="lunch-photo" role="img" aria-label="Photo of a chalkboard with a paper lunch bag, alarm clock, stacked books, coloured pencils and a red apple on a desk"></div>
  <div class="brand"><span class="brand__mark"></span><span class="brand__name">VELTRA</span></div>
  <h1 class="lunch-title">
    <span class="lunch-title__year">2018 Calendar</span>
    <span class="lunch-title__event">Lunch &amp;<br>Learn</span>
    <span class="lunch-title__tag">Life. Long. Learn</span>
  </h1>

  <div class="schedule">
    <div class="session col-1 row-1"><span class="session__month">MARCH:</span><span class="session__topic">Mindfulness</span></div>
    <div class="session col-1 row-2"><span class="session__month">APRIL:</span><span class="session__topic">Nutrition &amp;<br>Lifestyle Coaching</span></div>
    <div class="session col-1 row-3"><span class="session__month">MAY:</span><span class="session__topic">What is<br>Neuromodulation?</span></div>

    <div class="session col-2 row-1"><span class="session__month">JUNE:</span><span class="session__topic">Achieve Your Goals</span></div>
    <div class="session col-2 row-2"><span class="session__month">JULY:</span><span class="session__topic">Changing Your Life<br>PositiveThinking</span></div>
    <div class="session col-2 row-3"><span class="session__month">AUGUST:</span><span class="session__topic">Clean Eating How<br>Do I Get Started</span></div>

    <div class="session col-3 row-1"><span class="session__month">SEPTEMBER:</span><span class="session__topic">Budgeting 101<br>Financial Wellness</span></div>
    <div class="session col-3 row-2"><span class="session__month">OCTOBER:</span><span class="session__topic">Busted! Nutrition Myths</span></div>
    <div class="session col-3 row-3"><span class="session__month">NOVEMBER:</span><span class="session__topic">Time Management</span></div>
    <div class="session col-3 row-4"><span class="session__month">DECEMBER:</span><span class="session__topic">First Time Home Buyers</span></div>
  </div>
</section>

</body>
</html>
```